Kestrel Gardenworks Business Card

An eye catching, yet simple business card that includes;

1. our logo
2. office phone - 5083172946
3. email - kestrelgardenworks@mailbrook.com
4. website - www.kestrelgardenworks.com
5. instagram - @kestrelgardenworksnv

```html
<!DOCTYPE html>
<html lang="en">
<head>
<meta charset="utf-8">
<title>Kestrel Gardenworks Business Card</title>
<link href="https://fonts.googleapis.com/css2?family=Montserrat:wght@400;700&display=swap" rel="stylesheet">
<style>
  :root {
    --backdrop: #ababab;
    --card-light: #ffffff;
    --card-dark: #1f1a18;
    --pattern-tone: #231d1b;
    --ink: #1b1b1b;
    --accent: #a85f2a;
    --divider: #cfcfcf;
    --on-dark: #ffffff;
  }
  * { margin: 0; padding: 0; box-sizing: border-box; }
  html, body { width: 1200px; height: 1000px; overflow: hidden; }
  body {
    background: var(--backdrop);
    font-family: "Montserrat", sans-serif;
    position: relative;
  }
  .card {
    position: absolute;
    left: 294px;
    width: 613px;
    height: 352px;
    border-radius: 24px;
    overflow: hidden;
  }
  .card-front { top: 118px; background: var(--card-light); color: var(--ink); }
  .card-back { top: 525px; background: var(--card-dark); }

  .brand {
    position: absolute;
    display: flex;
    align-items: center;
    gap: 10px;
  }
  .brand-dot {
    flex: none;
    width: 18px; height: 18px;
    border-radius: 50%;
    background: var(--accent);
  }
  .brand-name {
    font-weight: 700;
    line-height: 1.05;
    color: var(--accent);
  }
  .card-front .brand { left: 42px; top: 128px; }
  .card-front .brand-name { font-size: 30px; }

  .divider {
    position: absolute;
    left: 306px; top: 127px;
    width: 1px; height: 113px;
    background: var(--divider);
  }
  .contact-list {
    position: absolute;
    left: 326px; top: 144px;
    list-style: none;
    font-size: 13px;
  }
  .contact-list li {
    display: flex; align-items: center;
    height: 20px; gap: 7px;
  }
  .contact-list svg { width: 10px; height: 10px; flex: none; fill: var(--accent); }
  .address {
    position: absolute;
    left: 0; right: 0; top: 314px;
    text-align: center;
    font-size: 13.5px;
    letter-spacing: 0.3px;
  }

  .pattern-area {
    position: absolute; inset: 0;
    background: linear-gradient(135deg, var(--pattern-tone), var(--card-dark));
  }
  .card-back .brand { left: 352px; top: 222px; }
  .card-back .brand-name { font-size: 19px; color: var(--on-dark); }
  .card-back .brand-dot { width: 12px; height: 12px; }
</style>
</head>
<body>

<section class="card card-front">
  <div class="brand">
    <span class="brand-dot"></span>
    <span class="brand-name">Kestrel<br>Gardenworks</span>
  </div>
  <div class="divider"></div>
  <ul class="contact-list">
    <li><svg viewBox="0 0 10 10"><path d="M2 0.5 L3.6 0.5 L4.2 2.8 L3 3.6 Q4 5.8 6.4 7 L7.2 5.8 L9.5 6.4 L9.5 8 Q9.5 9.5 8 9.5 Q0.5 9 0.5 2 Q0.5 0.5 2 0.5Z"/></svg>(508) 317-2946</li>
    <li><svg viewBox="0 0 10 10"><path d="M0.5 2 H9.5 V8 H0.5Z M0.5 2 L5 5.5 L9.5 2" fill="var(--accent)" stroke="#fff" stroke-width="0.8"/></svg>kestrelgardenworks@mailbrook.com</li>
    <li><svg viewBox="0 0 10 10"><circle cx="5" cy="5" r="4.3" fill="none" stroke="var(--accent)" stroke-width="1"/><ellipse cx="5" cy="5" rx="1.9" ry="4.3" fill="none" stroke="var(--accent)" stroke-width="0.9"/><path d="M0.7 5 H9.3" stroke="var(--accent)" stroke-width="0.9"/></svg>www.kestrelgardenworks.com</li>
    <li><svg viewBox="0 0 10 10"><rect x="0.8" y="0.8" width="8.4" height="8.4" rx="1.5"/></svg>@kestrelgardenworksnv</li>
  </ul>
  <p class="address">2317 Larkspur Ln Fallon, NV, 89406, United States</p>
</section>

<section class="card card-back">
  <div class="pattern-area" role="img" aria-label="Faint tiled brand pattern across the dark card back"></div>
  <div class="brand">
    <span class="brand-dot"></span>
    <span class="brand-name">Kestrel<br>Gardenworks</span>
  </div>
</section>

</body>
</html>
```